Wallet/Purse themed website design

We need a simple but visually stunning graphic design for a new web based company called "thecoinkeeper.net".

TheCoinKeeper is an online/phone app offering extremely secure backup/storage for our users' personal documentation, such as credit cards, ID, passports, certificates, insurance etc.

Documents will be uploaded via a mobile app (initially uDroid) to the storage. Retrieval is only possible via login together with bank level authentication (using personal questions).

Our service will not prevent the theft of our customer's physical wallet however our retrieval service can be accessed anywhere online and assist with the replacement. (for example a lost passport will require a new passport request which requires details of the lost passport number/details).
The key audiences for TheCoinKeeper include holidaymakers, businessmen, individuals, banking customers

We have specified that the initial design needs only to have 3 pages - home page, login page, wallet contents retrieval page.

Common themes of the following should be strongly brought to bear on the pages:
-Leather wallet/stitching
-Secure/safe/private/encryted
-Personal - for example family holiday
-Access anywhere
-Pick pockets can easily steal your wallet
Updates

Thank you for all of your submissions!  This was our first attempt to source a design via Sketch Hive and we will certainly use this resource again.

Thank you.

Target Market(s)

Industry/Entity Type

Graphic Design

Requirements
Must have
• 3 pages - home page, login page, wallet contents retrieval page.
Nice to have
• Modern UI design appealing to families and individuals

```html
<!DOCTYPE html>
<html lang="en">
<head>
<meta charset="utf-8">
<title>thecoinkeeper.net</title>
<link rel="stylesheet" href="https://fonts.googleapis.com/css2?family=Ubuntu:wght@400;500;700&family=Arimo:ital,wght@0,400;0,700;1,400&display=swap">
<style>
:root{
  --night:#1b1b1b;
  --night-deep:#111;
  --stripe:#222;
  --slate:#6a6a6a;
  --mist:#d8d8d8;
  --paper:#fff;
  --tab:#5c5c5c;
  --tab-ink:#e8e8e8;
  --nav:#8a8a8a;
  --gold:#f5c518;
  --flame:#e2471b;
  --amber:#f58a1f;
  --ink:#6b6b6b;
  --navy:#0d3a66;
  --red:#c8261b;
  --card:#f3f3f3;
  --line:#bdbdbd;
}
*{margin:0;padding:0;box-sizing:border-box}
html,body{width:1146px;height:1200px;overflow:hidden;background:var(--paper);font-family:"Arimo",Arial,sans-serif}
.canvas{position:relative;width:1146px;height:1200px}
.abs{position:absolute}

.hero{left:0;top:0;width:1146px;height:430px;background:repeating-linear-gradient(90deg,var(--night) 0 22px,var(--stripe) 22px 24px)}
.hero-base{left:0;top:336px;width:1146px;height:94px;background:var(--night-deep)}
.glow-area{left:545px;top:200px;width:170px;height:136px;background:radial-gradient(ellipse 50% 60% at 50% 60%,rgba(245,170,40,.75) 0,rgba(200,90,20,.35) 55%,rgba(27,27,27,0) 100%)}
.brand-mini{left:235px;top:38px;font-family:"Ubuntu",sans-serif;font-weight:700;font-size:17px;color:#9a9a9a}
.headline{left:50px;top:108px;font-family:"Ubuntu",sans-serif;font-weight:700;font-size:54px;color:var(--gold)}
.nav{left:736px;top:42px;display:flex;gap:26px;font-size:11px;color:var(--nav);list-style:none}
.social{top:76px;display:flex;align-items:center;gap:8px;color:#ddd;font-family:"Ubuntu",sans-serif;font-size:17px}
.social .dot{width:14px;height:14px;background:#ddd}
.social .ring{width:16px;height:16px;border-radius:50%;background:#59a7d8}
.hero-device{left:746px;top:146px;width:103px;height:192px;border-radius:12px;background:linear-gradient(180deg,#3a4a5c,#0e1218);border:3px solid #2a7fbf}
.buy{left:229px;top:355px;width:194px;height:52px;display:flex;align-items:center;border-radius:4px;background:linear-gradient(90deg,var(--flame),#d8371a 70%,var(--amber));color:#fff;font-family:"Ubuntu",sans-serif;font-weight:700;font-size:24px;padding-left:14px}
.buy .price{margin-left:auto;margin-right:16px;font-size:17px}

.divider{left:0;top:430px;width:1146px;height:39px;background:var(--slate)}
.showcase{left:0;top:469px;width:1146px;height:246px;background:var(--mist)}
.tab{width:190px;height:29px;text-align:center;line-height:27px;font-size:14px;font-weight:700;color:var(--tab-ink);clip-path:polygon(0 0,100% 0,88% 100%,12% 100%)}
.tab-dark{left:479px;top:469px;background:var(--tab)}
.tab-light{left:479px;top:715px;background:var(--mist);color:#5a5a5a}
.arrow{top:594px}
.slide{border-radius:10px}
.slide-tablet{left:254px;top:545px;width:189px;height:113px;background:linear-gradient(90deg,#f4f4f4 0 14%,#7a4a2a 30%,#c9a060 55%,#4a3a2a 85%,#f4f4f4 86%);border:2px solid #ddd}
.slide-wallet{left:542px;top:523px;width:94px;height:165px;background:linear-gradient(90deg,#e6e6e6,#fafafa 40%,#cfcfcf 70%,#eee);border-radius:6px}
.slide-phone{left:782px;top:492px;width:107px;height:212px;border-radius:16px;background:linear-gradient(180deg,#222 0 14%,#7fc0e8 14%,#3a80b8 80%,#222 80%)}

.access{left:0;top:715px;width:1146px;height:211px;background:var(--paper);border-left:1px solid #ccc;border-right:1px solid #ccc}
.login-card{left:463px;top:760px;width:204px;height:144px;background:#f5efd9;border:2px solid #d7cfb4;border-radius:4px;box-shadow:0 2px 4px rgba(0,0,0,.25)}
.login-title{width:100%;text-align:center;margin-top:4px;font-family:"Ubuntu",sans-serif;font-weight:700;font-size:14px;color:#333;letter-spacing:.5px}
.field{position:absolute;left:24px;width:160px;height:18px;background:#fff;border:1px solid #ccc;border-radius:3px;font-size:7px;color:var(--red);padding:4px 8px;font-style:italic}
.field::after{content:"";position:absolute;right:-1px;top:-1px;width:20px;height:18px;background:var(--flame);border-radius:0 3px 3px 0}
.login-btn{position:absolute;left:71px;top:108px;width:62px;height:20px;background:linear-gradient(#a8d24a,#5f9a1e);border-radius:3px;font-size:8px;font-weight:700;color:#234;text-align:center;line-height:20px}
.lost{position:absolute;left:0;width:100%;top:130px;text-align:center;font-size:6px;color:var(--red)}
.links{left:767px;top:762px;list-style:none;font-family:"Ubuntu",sans-serif;font-weight:500;font-size:16px;color:var(--ink)}
.links li{height:38px}
.links li:nth-child(2){height:37px}

.rule{left:0;top:926px;width:1146px;height:8px;background:#555}
.retrieval{left:0;top:934px;width:1146px;height:140px;background:var(--paper);border:1px solid #ccc;border-top:0}
.record{left:362px;top:958px;width:386px;height:106px;background:var(--card);border:1px solid var(--line);border-radius:4px;font-size:12px}
.record-tip{left:390px;top:1062px}
.record .name{position:absolute;left:132px;top:9px;color:var(--red);line-height:16px}
.record .act{position:absolute;font-style:italic;color:#777}

.footer{left:0;top:1117px;width:1146px;height:83px;background:var(--slate);border-top:3px solid #444}
.copy{left:230px;top:1151px;font-size:9px;color:#fff}
</style>
</head>
<body>
<div class="canvas">
  <header>
    <div class="abs hero"></div>
    <div class="abs glow-area" role="img" aria-label="Warm light flare behind the phone"></div>
    <div class="abs hero-base"></div>
    <div class="abs brand-mini">TheCoinKeeper</div>
    <ul class="abs nav"><li>HOME</li><li>CONTACT US</li><li>ABOUT US</li><li>STORE</li></ul>
    <div class="abs social" style="left:752px"><span class="dot"></span>Friendbook</div>
    <div class="abs social" style="left:930px"><span class="ring"></span>Chirper</div>
    <h1 class="abs headline">thecoinkeeper.net</h1>
    <div class="abs hero-device" role="img" aria-label="uDroid phone showing the app home screen"></div>
    <div class="abs buy">Buy Now <span class="price">$0</span></div>
  </header>

  <div class="abs divider"></div>

  <section>
    <div class="abs showcase"></div>
    <div class="abs tab tab-dark">WALLET BACKUP</div>
    <svg class="abs arrow" style="left:214px" width="16" height="22" viewBox="0 0 16 22"><path d="M12 3 4 11l8 8" fill="none" stroke="#333" stroke-width="3.5"/></svg>
    <svg class="abs arrow" style="left:916px" width="16" height="22" viewBox="0 0 16 22"><path d="M4 3l8 8-8 8" fill="none" stroke="#333" stroke-width="3.5"/></svg>
    <div class="abs slide slide-tablet" role="img" aria-label="Tablet in landscape showing a music album carousel"></div>
    <div class="abs slide slide-wallet" role="img" aria-label="White leather wallet with a strap"></div>
    <div class="abs slide slide-phone" role="img" aria-label="uDroid phone showing an app grid"></div>
  </section>

  <section>
    <div class="abs access"></div>
    <div class="abs tab tab-light">SECURE LOGIN</div>
    <div class="abs login-card">
      <div class="login-title">SECURE LOGIN</div>
      <div class="field" style="top:24px">Your Name</div>
      <div class="field" style="top:52px">Your Email</div>
      <div class="field" style="top:80px">••••••</div>
      <div class="login-btn">LOGIN ›</div>
      <div class="lost">Lost Your Password?</div>
    </div>
    <ul class="abs links"><li>Contact US</li><li>About US</li><li>FAQ</li><li>Store</li></ul>
    <svg class="abs" style="left:869px;top:760px" width="41" height="43" viewBox="0 0 41 43"><rect width="41" height="43" rx="6" fill="var(--navy)"/><path d="M13 10c-3 2-3 6 0 12s8 11 13 12c3 0 5-2 5-4l-5-4-3 2c-3-2-6-6-7-9l2-3-3-6z" fill="#fff"/></svg>
    <svg class="abs" style="left:874px;top:823px" width="28" height="32" viewBox="0 0 28 32"><ellipse cx="14" cy="16" rx="12" ry="14" fill="none" stroke="var(--navy)" stroke-width="2"/><path d="M9 12a5 5 0 1 1 6 5v3" fill="none" stroke="var(--navy)" stroke-width="2"/><circle cx="15" cy="24" r="1.5" fill="var(--navy)"/></svg>
    <svg class="abs" style="left:866px;top:871px" width="55" height="43" viewBox="0 0 55 43"><path d="M1 3h8l6 24h30l6-18H12" fill="none" stroke="var(--navy)" stroke-width="3"/><path d="M14 15h35M16 21h31M24 9v18M33 9v18M42 9v18" stroke="var(--navy)" stroke-width="2"/><circle cx="19" cy="37" r="4" fill="var(--navy)"/><circle cx="41" cy="37" r="4" fill="var(--navy)"/></svg>
  </section>

  <div class="abs rule"></div>

  <section>
    <div class="abs retrieval"></div>
    <div class="abs record">
      <div class="name">Name<br>Details</div>
      <span class="act" style="left:132px;top:58px">Back</span>
      <span class="act" style="left:241px;top:58px">Next</span>
      <span class="act" style="left:132px;top:89px">Edit</span>
      <span class="act" style="left:241px;top:89px">Delete</span>
    </div>
    <svg class="abs record-tip" width="16" height="10" viewBox="0 0 16 10"><path d="M0 0l8 9 8-9" fill="var(--card)" stroke="var(--line)"/></svg>
  </section>

  <footer>
    <div class="abs footer"></div>
    <p class="abs copy">Copyright © 2012. KNVS. All rights reserved.</p>
  </footer>
</div>
</body>
</html>
```